Accounting Practice Business Card Design

I have a logo I am happy for you to use in the design of the Business Card.
You can edit and change colours as you please, I am not fixated on it.
I am looking for a modern and clean overall feel for the finished design.

The business is a small accounting practice who thrives on word of mouth referrals and this card will be given to all current and prospect clients.

Industry/Entity Type

Accountant

Contact Information for Business Card

Marcus Elwin
Level 5, 8 Corvale Ridge Road
ASHGROVE RISE VIC 3187
Phone: 9481 3057
Email: melwin@mrfaccountants.com.au
Web: www.mrfaccountants.com.au

Font styles to use
Serif
Sans Serif

Colors
0555a3
3277b5
85acd3
0393ce
33a6d7
85cae6
00a990
33b8a4
9bcb3c

Requirements
Must have
• "The end to your tax problems begin with us"
• "A referral from you is our greatest compliment"
Nice to have
• Modern clean professional

```html
<!DOCTYPE html>
<html lang="en">
<head>
<meta charset="UTF-8">
<title>MRF Accountants — Business Card</title>
<link rel="stylesheet" href="https://fonts.googleapis.com/css2?family=Open+Sans:ital,wght@0,400;0,600;0,700;0,800;1,400;1,600&display=swap">
<style>
  :root {
    --stage: #1d1f22;
    --card-black: #141414;
    --card-white: #ffffff;
    --tab-grey: #e6e6e6;
    --ink: #111111;
    --ink-soft: #3a3a3a;
    --text-light: #e8e8e8;
    --silver: #b9b9b9;
  }
  * { box-sizing: border-box; margin: 0; padding: 0; }
  html, body {
    width: 1200px; height: 900px; overflow: hidden;
    background: var(--stage);
    font-family: "Open Sans", Arial, sans-serif;
  }
  .stage {
    width: 1200px; height: 900px;
    display: flex; align-items: center; justify-content: center; gap: 60px;
  }
  .card {
    position: relative;
    width: 525px; height: 300px;
    border-radius: 22px;
    overflow: hidden;
    background: var(--card-black);
    box-shadow: 0 18px 40px rgba(0,0,0,.55);
  }

  /* Front */
  .card-front .band {
    position: absolute; inset: 0 0 auto 0; height: 112px;
    background: var(--card-white);
  }
  .card-front .name-tab {
    position: absolute; left: 0; top: 0; width: 250px; height: 112px;
    background: var(--tab-grey);
    clip-path: polygon(0 0, 100% 0, 80% 100%, 0 100%);
  }
  .card-front .holder {
    position: absolute; left: 28px; top: 24px; color: var(--ink);
  }
  .holder .name {
    font-weight: 800; font-size: 19px; letter-spacing: .4px; text-transform: uppercase;
  }
  .holder .phone { font-size: 15px; color: var(--ink-soft); margin-top: 2px; }
  .card-front .wordmark {
    position: absolute; right: 34px; top: 38px;
    font-weight: 800; font-size: 30px; letter-spacing: .5px; color: var(--ink);
    display: flex; align-items: center; gap: 10px;
  }
  .wordmark .dot {
    width: 14px; height: 14px; background: var(--ink);
  }
  .card-front .contact {
    position: absolute; left: 28px; top: 140px;
    color: var(--text-light); font-size: 13.5px; line-height: 1.5; font-style: italic;
  }
  .contact .address { margin-top: 14px; }
  .card-front .quotes {
    position: absolute; right: 30px; top: 150px; width: 230px;
    color: var(--text-light); font-size: 15px; line-height: 1.35;
    font-style: italic; font-weight: 600; text-align: center;
  }
  .quotes p + p { margin-top: 18px; }

  /* Back */
  .card-back .mark {
    position: absolute; inset: 0;
    display: flex; flex-direction: column; align-items: center; justify-content: center;
    color: var(--silver); font-weight: 800; line-height: 1;
  }
  .mark .mark-name { font-size: 108px; letter-spacing: 2px; }
  .mark .mark-sub { font-size: 31px; letter-spacing: 3px; margin-top: 6px; }
</style>
</head>
<body>
<main class="stage">
  <section class="card card-front" aria-label="Business card front">
    <div class="band"></div>
    <div class="name-tab"></div>
    <div class="holder">
      <p class="name">Marcus Elwin</p>
      <p class="phone">9481 3057</p>
    </div>
    <div class="wordmark"><span class="dot"></span>MRF</div>
    <div class="contact">
      <p>melwin@mrfaccountants.com.au</p>
      <p>www.mrfaccountants.com.au</p>
      <p class="address">Level 5, 8 Corvale Ridge Road<br>ASHGROVE RISE VIC 3187</p>
    </div>
    <div class="quotes">
      <p>“The end to your tax problems begin with us.”</p>
      <p>“A referral from you is our greatest compliment.”</p>
    </div>
  </section>

  <section class="card card-back" aria-label="Business card back">
    <div class="mark">
      <span class="mark-name">MRF</span>
      <span class="mark-sub">ACCOUNTANTS</span>
    </div>
  </section>
</main>
</body>
</html>
```